NEW KNV Chatterly and Display ADS!

We need to do Social Media designs for KNV Institute of Working Crafts
Site URL: http://www.knvgrounds.com/
Chatterly URL: https://www.chatterlyhub.com/KNVinstituteofworkingcrafts/
Sizes Required
-1200x628 (Chatterly Link Post) No more than 20% text coverage - Quantity (2)
-600x600 (Chatterly Carousel Post) No more than 20% text coverage - Quantity (2 sets, 3 pictures)
Display Sizes: ( 2 sets)
160 x 600
300 x 50
300 x 250
300 x 600
320 x 50
728 x 90
Client is looking to focus more on the end goal of going to a trade school, not going back to school.
The ads should focus on the benefit of attending a trade school.
Watch these two videos to discover some of the inspiration for the campaign:
http://benharlowsite.com/2017/03/attn-again-a-4-yr-degree-is-not-the-best-path-for-all/
here is the video:
https://www.chatterlyhub.com/PeterMangoFinch/videos/20837465190283746/
Please note that we cannot have more than 20% text on the image, see Chatterly's guidelines here.
https://www.chatterlyhub.com/policies/ads#text_in_images
School

```html
<!DOCTYPE html>
<html lang="en">
<head>
<meta charset="utf-8">
<title>KNV Institute of Working Crafts – Train for a Real Career</title>
<link rel="stylesheet" href="https://fonts.googleapis.com/css2?family=Fredoka:wght@600&family=Montserrat:wght@500;700&display=swap">
<style>
  :root {
    --navy: #2c2e6e;
    --white: #ffffff;
    --ink: #2c2e6e;
    --black: #1a1a1a;
    --photo-dark: #140d08;
    --photo-mid: #4a2e16;
    --photo-warm: #b86e22;
    --photo-glow: #f0b045;
  }
  * { margin: 0; padding: 0; box-sizing: border-box; }
  html, body { width: 1200px; height: 628px; overflow: hidden; background: var(--white); }
  .ad {
    position: relative;
    width: 1200px;
    height: 628px;
    background: var(--white);
    font-family: "Montserrat", Arial, sans-serif;
    overflow: hidden;
  }
  .hero-photo { position: absolute; inset: 0; width: 1200px; height: 628px; }
  .title-bar {
    position: absolute; left: 0; top: 0; width: 1200px; height: 66px;
    background: var(--navy);
    display: flex; align-items: center; justify-content: center;
  }
  .title-bar h1 {
    font-family: "Fredoka", "Arial Rounded MT Bold", sans-serif;
    font-weight: 600; font-size: 37px; color: var(--white); letter-spacing: 0.2px;
  }
  .brand {
    position: absolute; left: 34px; top: 96px; height: 50px;
    display: flex; align-items: center; gap: 10px;
  }
  .brand-square { width: 16px; height: 16px; background: var(--navy); }
  .brand-name {
    font-family: "Montserrat", Arial, sans-serif; font-weight: 700;
    font-size: 36px; color: var(--navy);
  }
  .offer { position: absolute; left: 28px; top: 208px; color: var(--ink); }
  .offer h2 { font-weight: 700; font-size: 31px; letter-spacing: 0.2px; line-height: 1; }
  .offer .benefit {
    margin: 12px 0 0 22px; font-weight: 700; font-size: 17px; line-height: 1;
  }
  .perks {
    position: absolute; left: 0; top: 296px; width: 528px;
    text-align: center; color: var(--black);
    font-weight: 700; font-size: 18px; line-height: 26px; letter-spacing: 0.3px;
  }
  .phone-band {
    position: absolute; left: 0; top: 383px; width: 560px; height: 66px;
    background: var(--navy); color: var(--white);
    display: flex; align-items: center; padding-left: 96px;
    font-weight: 700; font-size: 40px; letter-spacing: 0.3px;
  }
  .url-band {
    position: absolute; left: 0; top: 584px; width: 600px; height: 44px;
    background: var(--navy); color: var(--white);
    display: flex; align-items: center; padding-left: 108px;
    font-weight: 500; font-size: 23px; letter-spacing: 0.3px;
  }
</style>
</head>
<body>
<main class="ad">
  <svg class="hero-photo" viewBox="0 0 1200 628">
    <defs>
      <radialGradient id="weld-glow" cx="0.25" cy="0.95" r="0.9">
        <stop offset="0" stop-color="var(--photo-glow)"/>
        <stop offset="0.25" stop-color="var(--photo-warm)"/>
        <stop offset="0.55" stop-color="var(--photo-mid)"/>
        <stop offset="1" stop-color="var(--photo-dark)"/>
      </radialGradient>
      <clipPath id="photo-clip">
        <path d="M602 66 C 505 250, 505 450, 590 628 L1200 628 L1200 66 Z"/>
      </clipPath>
    </defs>
    <rect role="img" aria-label="Photo of a welder in goggles and leather gloves cutting metal with a gas torch, sparks flying" x="500" y="66" width="700" height="562" fill="url(#weld-glow)" clip-path="url(#photo-clip)"/>
    <path d="M602 66 C 505 250, 505 450, 590 628" fill="none" stroke="var(--navy)" stroke-width="10"/>
  </svg>

  <header class="title-bar">
    <h1>Chicago’s Best Welding &amp; HVAC/R Trade School</h1>
  </header>

  <div class="brand">
    <span class="brand-square"></span>
    <span class="brand-name">KNV</span>
  </div>

  <section class="offer">
    <h2>TRAIN FOR A REAL CAREER</h2>
    <p class="benefit">SKILLED JOBS IN MONTHS, NOT YEARS</p>
  </section>

  <p class="perks">NO 4-YEAR DEGREE NEEDED<br>&amp; LESS STUDENT DEBT</p>

  <div class="phone-band">555-318-2740</div>

  <footer class="url-band">www.knvgrounds.com</footer>
</main>
</body>
</html>
```